Gooey Glow

I am creating an online slime shop that will sell handmade custom slimes. I need to be able to have payment/shipping options and the ability to change product photos since the product and product name will change often

Target Market(s)

Slime

Industry/Entity Type

Retail - online sales

Coding

Coded - Design and coding required

Number of Pages Required

2 page

Font styles to use
Sans Serif

Colors
0094D4
00A9DD
6FCCEA
C7EBF8
E9F6FB
E54698
E96AAD
F1A4CE
F9D9EA
FCEFF6
A7469A
B969AE
D3A5CF
EDDBEB
F8F0F9

Requirements
Must have
• My logo, my domain, ability to change photos of products for sale, payment options, shipping options, social media links, contact us,

```html
<!DOCTYPE html>
<html lang="en">
<head>
<meta charset="utf-8">
<title>Gooey Glow – Handmade Custom Slimes</title>
<link rel="stylesheet" href="https://fonts.googleapis.com/css2?family=Montserrat:wght@400;500;600;700&family=Lato:wght@400;700&display=swap">
<style>
:root{
  --teal:#8dd5dc;
  --teal-deep:#86d1d6;
  --teal-line:#9ddfe0;
  --magenta:#c8418a;
  --violet:#9b30c4;
  --purple:#a7469a;
  --blush:#f4d9e8;
  --blue:#0094d4;
  --ink:#1a1a1a;
  --white:#ffffff;
}
*{margin:0;padding:0;box-sizing:border-box}
html,body{width:1200px;height:3392px;overflow:hidden;background:var(--white)}
body{position:relative;font-family:'Lato',sans-serif;color:var(--ink)}
.abs{position:absolute}
.wave{position:absolute;left:0;width:1200px}

/* nav */
.nav a{position:absolute;top:50px;font:500 18px 'Montserrat',sans-serif;color:var(--ink);text-decoration:none;letter-spacing:.2px}
.nav a.active{color:var(--magenta)}
.brand{position:absolute;display:flex;align-items:center;gap:10px;font:700 22px 'Montserrat',sans-serif;color:var(--purple);white-space:nowrap}
.brand .dot{width:34px;height:34px;border-radius:50%;background:var(--ink)}

.btn{position:absolute;display:flex;align-items:center;justify-content:center;background:var(--blue);color:var(--white);border-radius:20px;border-bottom:3px solid var(--magenta);font:700 17px 'Montserrat',sans-serif}

/* hero */
.hero-kicker{left:113px;top:183px;font:500 22px 'Montserrat',sans-serif}
.hero-title{left:107px;top:214px;font:600 45px 'Montserrat',sans-serif;color:var(--violet)}
.hero-text{left:113px;top:272px;width:440px;font:400 16px/26px 'Montserrat',sans-serif}
.hero-art{left:600px;top:80px;width:600px;height:520px;border-radius:48% 40% 10% 10%;background:radial-gradient(circle at 45% 55%,#f0509f 0%,#e54698 45%,rgba(229,70,152,0) 72%)}

/* featured */
.section-title{font:600 38px 'Montserrat',sans-serif;text-align:center;letter-spacing:.5px}
.section-title span{color:var(--magenta)}
.intro{left:250px;top:768px;width:700px;text-align:center;font:400 14.5px/23px 'Lato',sans-serif}
.product-photo{position:absolute;border-radius:50%;border:4px solid var(--white)}
.arrow{position:absolute;width:36px;height:36px;border-radius:50%;background:#111;display:flex;align-items:center;justify-content:center}
.product{position:absolute;top:1298px;width:290px;text-align:center}
.product h3{font:500 26px 'Montserrat',sans-serif;color:var(--violet);margin-bottom:14px}
.product p{font:400 14.5px/23px 'Lato',sans-serif}

/* about */
.about-art{left:125px;top:1665px;width:345px;height:495px;border-radius:45% 45% 12% 12%;background:radial-gradient(circle at 50% 50%,#ffffff 0 38%,#1b1b1b 62%)}
.about-title{left:563px;top:1688px;font:600 38px 'Montserrat',sans-serif}
.about-title span{color:var(--magenta)}
.about-rule{left:568px;top:1742px}
.about-text{left:567px;top:1786px;width:500px;font:400 16px/26px 'Montserrat',sans-serif;color:#2a2a2a}
.about-text p+p{margin-top:10px}

/* testimonials */
.testimonial{left:60px;top:2348px;width:1080px;height:404px;border-radius:202px;background:linear-gradient(180deg,#8e3bc9 0%,#b0439f 55%,#c9468f 100%);color:var(--white)}
.testimonial h2{position:absolute;top:78px;width:100%;text-align:center;font:600 38px 'Montserrat',sans-serif}
.testimonial .quote{position:absolute;top:151px;left:183px;width:720px;text-align:center;font:400 18px/25px 'Lato',sans-serif}
.testimonial .who{position:absolute;top:230px;width:100%;text-align:center;font:400 19px 'Lato',sans-serif}
.qmark{position:absolute;font:700 56px/1 'Montserrat',sans-serif;color:var(--white)}
.dots{position:absolute;top:312px;left:498px;display:flex;gap:8px}
.dots i{display:block;width:22px;height:6px;background:var(--white)}

/* footer */
.foot-h{font:500 25px 'Montserrat',sans-serif;color:var(--white)}
.pay{position:absolute;top:3058px;display:flex;gap:6px}
.pay span{width:54px;height:30px;background:var(--white);border-radius:3px;display:flex;align-items:center;justify-content:center;font:600 9.5px 'Montserrat',sans-serif;color:#333}
.social{position:absolute;left:778px;top:3064px;display:flex;gap:9px;font:500 12.5px 'Montserrat',sans-serif;color:var(--white)}
.contact{position:absolute;top:3171px;display:flex;align-items:center;gap:14px;font:500 17px 'Montserrat',sans-serif;color:var(--white)}
.contact .ic{width:40px;height:40px;border-radius:50%;background:linear-gradient(135deg,#8e3bc9,#e54698);display:flex;align-items:center;justify-content:center}
.foot-rule{left:110px;top:3251px;width:980px;height:1px;background:rgba(255,255,255,.7)}
.copy{top:3296px;width:1200px;text-align:center;font:500 18px 'Montserrat',sans-serif;color:var(--white)}
</style>
</head>
<body>

<!-- HERO -->
<svg class="wave" style="top:0" height="640" viewBox="0 0 1200 640">
  <defs>
    <linearGradient id="heroTeal" x1="0" y1="0" x2="1" y2="1">
      <stop offset="0" stop-color="#93d9df"/><stop offset=".5" stop-color="#84d0d6"/><stop offset="1" stop-color="#95dadf"/>
    </linearGradient>
  </defs>
  <path d="M0 0H1200V560C1020 520 840 525 620 565C420 605 220 610 0 545Z" fill="url(#heroTeal)"/>
  <path d="M0 555C200 615 420 625 620 580C840 535 1020 520 1200 575" fill="none" stroke="var(--magenta)" stroke-width="14"/>
</svg>
<div class="abs hero-art" role="img" aria-label="Pink slime panda with a hand stretching slime above it"></div>

<nav class="nav">
  <a class="active" style="left:111px">HOME</a>
  <a style="left:220px">ABOUT US</a>
  <a style="left:369px">PRODUCTS</a>
  <a style="left:734px">BLOG</a>
  <a style="left:837px">CONTACT US</a>
</nav>
<div class="brand" style="left:520px;top:45px"><span class="dot"></span>Gooey Glow</div>
<svg class="abs" style="left:1019px;top:52px" width="16" height="16" viewBox="0 0 16 16"><circle cx="8" cy="5" r="4" fill="#111"/><path d="M1 16C1 11 4 9 8 9S15 11 15 16Z" fill="#111"/></svg>
<svg class="abs" style="left:1071px;top:52px" width="18" height="16" viewBox="0 0 18 16"><path d="M0 1H3L5 11H15L17 4H4" fill="none" stroke="#111" stroke-width="2"/><rect x="5" y="4" width="11" height="6" fill="#111"/><circle cx="6" cy="14" r="1.6" fill="#111"/><circle cx="14" cy="14" r="1.6" fill="#111"/></svg>

<div class="abs hero-kicker">Handmade</div>
<h1 class="abs hero-title">Custom Slimes</h1>
<p class="abs hero-text">Lorem ipsum dolor sit amet, consectetur adipiscing elit, sed do eiusmod tempor incididunt ut labore et dolore magna aliqua.</p>
<div class="btn" style="left:108px;top:365px;width:138px;height:40px">Buy Now</div>

<!-- FEATURED -->
<h2 class="abs section-title" style="left:0;top:705px;width:1200px">FEATURED <span>PRODUCTS</span></h2>
<p class="abs intro">Lorem ipsum dolor sit amet, consectetur adipiscing elit, sed do eiusmod tempor incididunt ut labore et dolore magna aliqua. Quis ipsum suspendisse ultrices gravida. Risus commodo viverra maecenas accumsan lacus vel facilisis.</p>

<div class="product-photo" role="img" aria-label="Blue slime jar with panda toppers and disco balls" style="left:112px;top:895px;width:370px;height:370px;background:radial-gradient(circle at 50% 40%,#b9c9cc,#7fa3ad 70%,#53707a)"></div>
<div class="product-photo" role="img" aria-label="Purple slime jar with pink waffle topper" style="left:715px;top:895px;width:370px;height:370px;background:radial-gradient(circle at 50% 45%,#f0a9b8,#e0728f 55%,#c9a45c)"></div>
<div class="product-photo" role="img" aria-label="Pink slime jar with waffle and sprinkles" style="left:400px;top:869px;width:400px;height:400px;background:linear-gradient(180deg,#f2c6c8 0%,#eab0b8 45%,#d56ab2 70%,#c44ea6 100%)"></div>

<div class="arrow" style="left:52px;top:1062px"><svg width="12" height="14" viewBox="0 0 12 14"><path d="M9 1L3 7L9 13" fill="none" stroke="#fff" stroke-width="2.4"/></svg></div>
<div class="arrow" style="left:1112px;top:1062px"><svg width="12" height="14" viewBox="0 0 12 14"><path d="M3 1L9 7L3 13" fill="none" stroke="#fff" stroke-width="2.4"/></svg></div>

<div class="product" style="left:152px"><h3>Slime 1</h3><p>Lorem ipsum dolor sit amet, consectetur adipiscing elit, sed do eiusmod tempor incididunt ut labore et dolore aliqua.</p></div>
<div class="product" style="left:454px"><h3>Slime 2</h3><p>Lorem ipsum dolor sit amet, consectetur adipiscing elit, sed do eiusmod tempor incididunt ut labore et dolore aliqua.</p></div>
<div class="product" style="left:755px"><h3>Slime 3</h3><p>Lorem ipsum dolor sit amet, consectetur adipiscing elit, sed do eiusmod tempor incididunt ut labore et dolore aliqua.</p></div>
<div class="btn" style="left:534px;top:1443px;width:132px;height:40px;font-size:17px">Shop Now</div>

<!-- ABOUT -->
<svg class="wave" style="top:1520px" height="740" viewBox="0 0 1200 740">
  <path d="M0 40C220 110 420 95 620 55C840 10 1020 10 1200 55V640C1020 590 820 600 620 640C420 680 220 690 0 640Z" fill="var(--blush)"/>
  <path d="M0 40C220 115 420 100 620 58C840 12 1020 10 1200 52" fill="none" stroke="var(--teal-line)" stroke-width="14"/>
  <path d="M0 650C220 705 420 700 620 655C820 612 1020 600 1200 650" fill="none" stroke="var(--teal-line)" stroke-width="14"/>
</svg>
<div class="abs about-art" role="img" aria-label="Black and white panda illustration"></div>
<h2 class="abs about-title">ABOUT <span>US</span></h2>
<svg class="abs about-rule" width="140" height="18" viewBox="0 0 140 18"><path d="M2 14C40 8 90 6 138 4M20 10C60 6 100 5 135 8" fill="none" stroke="#111" stroke-width="2.5"/></svg>
<div class="abs about-text">
  <p>Sed ut perspiciatis unde omnis iste natus error sit voluptatem accusantium doloremque laudantium, totam rem aperiam, eaque ipsa quae ab illo inventore veritatis et quasi architecto beatae vitae dicta sunt explicabo. Nemo enim ipsam voluptatem quia voluptas sit aspernatur aut odit aut fugit, sed quia consequuntur magni dolores eos qui ratione voluptatem sequi nesciunt.</p>
  <p>Sed ut perspiciatis unde omnis iste natus error sit voluptatem accusantium doloremque laudantium</p>
</div>
<div class="btn" style="left:572px;top:2046px;width:132px;height:40px">Shop Now</div>

<!-- TESTIMONIALS -->
<section class="abs testimonial">
  <h2>OUR TESTIMONIALS</h2>
  <span class="qmark" style="left:136px;top:128px">“</span>
  <p class="quote">Lorem ipsum dolor sit amet, consectetur adipiscing elit, sed do eiusmod tempor incididunt ut labore et dolore magna aliqua. Ut enim ad minim veniam, quis nostrud exercitation ullamco laboris nisi ut aliquip ex ea commodo consequat.</p>
  <span class="qmark" style="left:776px;top:212px">”</span>
  <p class="who">Maya T.</p>
  <div class="dots"><i></i><i></i><i></i></div>
</section>

<!-- FOOTER -->
<svg class="wave" style="top:2810px" height="582" viewBox="0 0 1200 582">
  <path d="M0 60C220 130 420 120 620 80C820 40 1020 40 1200 90V582H0Z" fill="var(--teal-deep)"/>
  <path d="M0 12C200 95 420 108 620 60C820 15 1020 15 1200 75" fill="none" stroke="var(--magenta)" stroke-width="14"/>
</svg>
<div class="abs foot-h" style="left:160px;top:3008px">Payment</div>
<div class="pay" style="left:161px"><span>Paywell</span><span>Cardmark</span><span>Vestra</span><span>Maxto</span></div>
<div class="brand" style="left:497px;top:3040px;color:var(--purple)"><span class="dot"></span>Gooey Glow</div>
<div class="abs foot-h" style="left:778px;top:3008px">Social Media</div>
<div class="social"><span>Glimmr</span><span>Fanbook</span><span>Chirp</span><span>Vidtube</span><span>Tikdance</span></div>

<div class="contact" style="left:185px"><span class="ic"><svg width="16" height="16" viewBox="0 0 16 16"><path d="M3 1L6 1L7 5L5 6C6 8 8 10 10 11L11 9L15 10L15 13C15 14 14 15 13 15C6 15 1 10 1 3C1 2 2 1 3 1Z" fill="#fff"/></svg></span>555-010-2468</div>
<div class="contact" style="left:458px"><span class="ic"><svg width="16" height="12" viewBox="0 0 16 12"><rect width="16" height="12" rx="1.5" fill="#fff"/><path d="M1 1L8 7L15 1" fill="none" stroke="#b0439f" stroke-width="1.6"/></svg></span>hello@gooeyglow.shop</div>
<div class="contact" style="left:835px"><span class="ic"><svg width="16" height="16" viewBox="0 0 16 16"><circle cx="8" cy="8" r="7" fill="#fff"/><ellipse cx="8" cy="8" rx="3" ry="7" fill="none" stroke="#b0439f" stroke-width="1.2"/><path d="M1 8H15" stroke="#b0439f" stroke-width="1.2"/></svg></span>gooeyglow.shop</div>

<div class="abs foot-rule"></div>
<p class="abs copy">© 2024 Gooey Glow. All Rights Reserved.</p>

</body>
</html>
```